Remodeling brochure

We need an informative homeowner friendly brochure detailing our company and things we do. We are looking for an initial setup and ideas (# of pages, etc) and then we will send more content. We are uploading our logo design. We are a high end remodeling company specializing in kitchen & bath remodels. We sell ourselves on customer communication and attention to detail in our designs and remodels.

Target Market(s)

Residential homeowners

Contact Information for Business Card

Modern and attention grabbing

Requirements
Must have
• Name- Hearth & Tile Crafters<br/>Address- 728 NW Folley Lane Suite #217<br/> Ankeny, Iowa 50388<br/>Phone- 515-472-8093<br/>email-htcrafterspro@mailvane.net

```html
<!DOCTYPE html>
<html lang="en">
<head>
<meta charset="utf-8">
<title>Hearth &amp; Tile Crafters — Brochure</title>
<link href="https://fonts.googleapis.com/css2?family=Poppins:wght@400;500;600;700;800&family=Roboto:wght@400;500&display=swap" rel="stylesheet">
<style>
:root{
  --brand-blue:#1a5bbf;
  --band-blue:#2a9be6;
  --deep-blue:#123f86;
  --scene-grey:#dedede;
  --paper:#ffffff;
  --ink:#333333;
  --body-grey:#666666;
  --accent-green:#7ab648;
  --rule:#cfcfcf;
}
*{box-sizing:border-box;margin:0;padding:0}
html,body{width:1200px;height:4813px;overflow:hidden}
body{background:var(--paper);font-family:"Roboto",Arial,sans-serif;color:var(--ink)}

.site-header{height:248px;display:flex;align-items:center;justify-content:center;gap:18px;background:var(--paper)}
.brand-square{width:64px;height:64px;background:var(--brand-blue)}
.brand-name{font-family:"Poppins",Arial,sans-serif;font-weight:600;color:var(--brand-blue);font-size:42px;letter-spacing:.5px}

.panel{height:1140px;background:var(--scene-grey);margin-top:8px;display:flex;align-items:center;justify-content:center}
.panel.last{height:1117px}

.page{position:relative;background:var(--paper);border:1px solid var(--rule);overflow:hidden}
.spread{display:flex}
.spread .page{width:450px;height:680px}
.spread .page + .page{border-left:none}
.cover-solo{width:520px;height:760px;font-size:16px}
.spread .cover{font-size:14px}

.photo{position:absolute}
.frame{position:absolute;background:var(--paper);padding:.4em;box-shadow:0 0 0 1px var(--rule)}
.frame .fill{width:100%;height:100%}

/* cover */
.cover .logo{position:absolute;top:6%;left:0;right:0;display:flex;justify-content:center;align-items:center;gap:.6em}
.logo-square{width:1.8em;height:1.8em;background:var(--brand-blue)}
.logo-name{font-family:"Poppins",Arial,sans-serif;font-weight:600;color:var(--brand-blue);font-size:1.1em}
.cover .hero{left:7.7%;width:84.6%;top:17%;height:32%;background:linear-gradient(180deg,#3c4a5c 0%,#5e6d80 45%,#d9d3bf 100%)}
.cover .band{position:absolute;left:7.7%;width:84.6%;top:28%;height:10%;background:var(--band-blue);display:flex;align-items:center;justify-content:center;text-align:center;color:#fff;font-family:"Poppins",Arial,sans-serif;font-weight:600;font-size:.85em;line-height:1.35;text-transform:uppercase}
.cover .f1{left:7.7%;top:55%;width:25%;height:18%}
.cover .f2{left:37%;top:58%;width:25%;height:17%}
.cover .f3{left:67%;top:54%;width:25.3%;height:21%}
.tone-dark{background:linear-gradient(160deg,#2b2d33,#6a6e78)}
.tone-warm{background:linear-gradient(160deg,#3d352e,#b49a7c)}
.tone-blue{background:linear-gradient(160deg,#1e4f8c,#cfe2f2)}
.cover .web{position:absolute;right:8%;bottom:4%;font-size:.7em;color:var(--body-grey)}

/* back cover */
.back .logo{position:absolute;top:55%;left:0;right:0;display:flex;justify-content:center;align-items:center;gap:8px;font-size:14px}
.back .title{position:absolute;top:63%;left:0;right:0;text-align:center;font-family:"Poppins",Arial,sans-serif;font-size:20px;color:var(--ink)}
.back .contacts{position:absolute;top:78%;left:6%;right:6%;font-size:8.5px;color:var(--body-grey)}
.contact-row{display:flex;justify-content:space-between;align-items:center;padding:6px 0;border-bottom:1px solid #e6e6e6}
.contact-row span{display:flex;align-items:center;gap:4px}
.contact-row b{color:var(--brand-blue);font-weight:500}
.dot{width:6px;height:6px;border-radius:50%;background:var(--accent-green)}
.dot.blue{background:var(--brand-blue)}

/* about spread */
.about{position:absolute;left:0;top:0;bottom:0;width:170px;padding:34px 0 28px 24px}
.about h2{font-family:"Poppins",Arial,sans-serif;font-weight:800;color:var(--deep-blue);font-size:30px;line-height:1;border-left:4px solid var(--deep-blue);padding-left:10px;margin-left:6px}
.about .copy{margin-top:24px;font-size:7px;line-height:1.6;color:var(--body-grey);text-align:justify}
.about .copy p{margin-bottom:9px}
.about .copy strong{color:var(--brand-blue);font-weight:500}
.about .copy h3{color:var(--accent-green);font-weight:500;font-size:7.5px;margin-bottom:2px}
.about-photo{position:absolute;top:28px;bottom:28px;background:linear-gradient(180deg,#9fc2ea 0%,#3b6fb2 55%,#1c3d6e 100%)}
.about-photo.left-half{left:186px;right:0}
.about-photo.right-half{left:0;right:28px}

/* inner */
.inner{display:flex;flex-direction:column;padding:30px 26px 34px;font-size:8.5px;line-height:1.6;color:var(--body-grey)}
.inner h2{font-family:"Poppins",Arial,sans-serif;font-size:13px;font-weight:600;color:var(--brand-blue)}
.inner h4{color:var(--brand-blue);font-weight:500;font-size:9px;margin:12px 0 3px}
.inner .greet{font-size:9px;color:var(--ink);margin:2px 0 4px}
.inner p{text-align:justify}
.inner ul{list-style:none}
.inner li::before{content:"• ";color:var(--brand-blue)}
.cols{display:grid;grid-template-columns:1fr 1fr;column-gap:22px}
.inner-photo{margin-top:auto;height:140px;flex-shrink:0;background:linear-gradient(160deg,#2d3138,#e8e8ea 70%)}
.grid-photo{position:absolute}
.g1{left:36px;top:40px;width:170px;height:290px;background:linear-gradient(180deg,#e6eef4,#7aa9d0 55%,#b48a4e)}
.g2{left:240px;top:40px;width:170px;height:140px;background:linear-gradient(160deg,#1f5aa3,#c9def0)}
.g3{left:240px;top:200px;width:170px;height:340px;background:linear-gradient(180deg,#f2f2f2,#bfbfbf 50%,#2a2a2a)}
.g4{left:36px;top:350px;width:170px;height:190px;background:linear-gradient(180deg,#f5f5f5,#9a9a9a 60%,#3a3a3a)}
.inner-url{position:absolute;left:36px;right:40px;bottom:34px;text-align:center;font-size:7px;color:var(--body-grey)}
</style>
</head>
<body>

<header class="site-header">
  <div class="brand-square"></div>
  <div class="brand-name">HEARTH &amp; TILE CRAFTERS</div>
</header>

<section class="panel">
  <div class="page cover cover-solo">
    <div class="logo"><div class="logo-square"></div><div class="logo-name">HEARTH &amp; TILE CRAFTERS</div></div>
    <div class="photo hero" role="img" aria-label="Modern kitchen with dark tile backsplash and range hood"></div>
    <div class="band">Smart home trend in the future<br>and enjoy your life</div>
    <div class="frame f1"><div class="fill tone-warm" role="img" aria-label="Kitchen interior with glass cabinets"></div></div>
    <div class="frame f2"><div class="fill tone-dark" role="img" aria-label="Dark modern bathroom"></div></div>
    <div class="frame f3"><div class="fill tone-blue" role="img" aria-label="Bright blue bathroom with tub"></div></div>
    <div class="web">www.hearthtilecrafters.com</div>
  </div>
</section>

<section class="panel">
  <div class="spread">
    <div class="page back">
      <div class="logo"><div class="logo-square"></div><div class="logo-name">HEARTH &amp; TILE CRAFTERS</div></div>
      <div class="title">Contact Us</div>
      <div class="contacts">
        <div class="contact-row">
          <span>
            <svg width="8" height="10" viewBox="0 0 8 10"><path d="M4 0a4 4 0 0 1 4 4c0 3-4 6-4 6S0 7 0 4a4 4 0 0 1 4-4z" fill="#1a5bbf"/><circle cx="4" cy="4" r="1.4" fill="#fff"/></svg>
            <b>Address:</b> 728 NW Folley Lane Suite #217, Ankeny, Iowa 50388</span>
          <span>
            <svg width="9" height="9" viewBox="0 0 10 10"><path d="M2 0l2 2.5-1.2 1.3a6 6 0 0 0 3.4 3.4L7.5 6 10 8l-1.3 1.6C4.5 10 0 5.5.4 1.3z" fill="#1a5bbf"/></svg>
            <b>Phone No:</b> 515-472-8093</span>
        </div>
        <div class="contact-row">
          <span><i class="dot blue"></i>@hearthtilecrafters</span>
          <span><i class="dot"></i>www.hearthtilecrafters.com</span>
          <span><i class="dot blue"></i>@htcrafters</span>
          <span><i class="dot"></i>htcrafterspro@mailvane.net</span>
        </div>
      </div>
    </div>
    <div class="page cover">
      <div class="logo"><div class="logo-square"></div><div class="logo-name">HEARTH &amp; TILE CRAFTERS</div></div>
      <div class="photo hero" role="img" aria-label="Modern kitchen with dark tile backsplash and range hood"></div>
      <div class="band">Smart home trend in the future<br>and enjoy your life</div>
      <div class="frame f1"><div class="fill tone-warm" role="img" aria-label="Kitchen interior with glass cabinets"></div></div>
      <div class="frame f2"><div class="fill tone-dark" role="img" aria-label="Dark modern bathroom"></div></div>
      <div class="frame f3"><div class="fill tone-blue" role="img" aria-label="Bright blue bathroom with tub"></div></div>
      <div class="web">www.hearthtilecrafters.com</div>
    </div>
  </div>
</section>

<section class="panel">
  <div class="spread">
    <div class="page">
      <div class="about">
        <h2>About<br>Us</h2>
        <div class="copy">
          <p><strong>HTCrafters</strong> plans and builds kitchens and baths for homeowners who care about the details. We listen first, sketch often and keep you informed at every stage, from the first visit to the final walkthrough of your new room.</p>
          <p>Our crews treat each home with respect, protect your floors and clean up daily. Cabinets, tile, lighting and plumbing are planned together so every piece fits the way you live.</p>
          <h3>HTCrafters Group</h3>
          <p>We are a small team of designers and builders based in Ankeny. Every project has one lead who answers your calls and walks you through choices, costs and timelines.</p>
          <p>If you want a kitchen that works harder or a bath that feels like a retreat, we bring clear plans, honest pricing and careful finish work on every job.</p>
          <p>Let us help you turn ideas into rooms you enjoy every single day.</p>
        </div>
      </div>
      <div class="about-photo left-half" role="img" aria-label="White shaker kitchen with blue tile and stainless appliances"></div>
    </div>
    <div class="page">
      <div class="about-photo right-half" role="img" aria-label="White shaker kitchen with blue tile and stainless appliances, continued"></div>
    </div>
  </div>
</section>

<section class="panel last">
  <div class="spread">
    <div class="page inner">
      <h2>HTCrafters</h2>
      <div class="greet">Hi, Homeowner</div>
      <p>Thank you for considering us for your remodel. This guide explains how we work, what to expect and how we keep your project on schedule and on budget from start to finish.</p>
      <h4>BENEFITS</h4>
      <ul>
        <li>Free design consultation</li>
        <li>Clear written estimates</li>
        <li>Single project lead</li>
        <li>Quality materials and finishes</li>
        <li>Workmanship warranty on every job</li>
        <li>Weekly progress updates</li>
      </ul>
      <div class="cols">
        <div>
          <h4>Attention:</h4>
          <p>We review every detail before work starts, from outlet placement to grout color, so surprises stay small and decisions stay easy.</p>
          <h4>Kitchen History:</h4>
          <p>You don't have to erase the charm of an older home. We blend new function with original character and lasting materials.</p>
        </div>
        <div>
          <h4>No boundaries:</h4>
          <p>There is no room too small or layout too tricky. We find smart storage and better flow in any space you have.</p>
          <h4>24/7 Availability:</h4>
          <p>Reach your project lead by phone or email any time, and we reply within one business day, every day.</p>
        </div>
      </div>
      <div class="inner-photo" role="img" aria-label="Open white kitchen with dining area"></div>
    </div>
    <div class="page">
      <div class="grid-photo g1" role="img" aria-label="Kitchen island with pendant light and bar stools"></div>
      <div class="grid-photo g2" role="img" aria-label="Blue and white bathroom vanity"></div>
      <div class="grid-photo g3" role="img" aria-label="Marble bathroom with black sink"></div>
      <div class="grid-photo g4" role="img" aria-label="White kitchen cabinets with range"></div>
      <div class="inner-url">www.hearthtilecrafters.com</div>
    </div>
  </div>
</section>

</body>
</html>
```